cup design rebranding with modern design

8 oz and 4 oz cup redesign

i will share my existing cups

also i want different slogans for coffee on the back also my logo is attached any color also a design for take away holder

be creative

modern

and elegant

i need it to be innovative

Industry/Entity Type

Coffee Shop

Font styles to use
Decorative
Script

Colors

Designer to choose colors to be used in the design.

Requirements
Must have
• logo
• instagram account @marlowbrewhouse
• slogan english or arabic

```html
<!DOCTYPE html>
<html lang="en">
<head>
<meta charset="utf-8">
<title>Marlow Cup Wrap</title>
<link href="https://fonts.googleapis.com/css2?family=Josefin+Sans:wght@300;400;700&family=Dancing+Script:wght@600&display=swap" rel="stylesheet">
<style>
  :root {
    --paper: #f6f4f0;
    --brown: #5a2d12;
    --brown-soft: #7a4526;
    --pattern: #ece6df;
    --charcoal: #2f2b2a;
    --cream: #f3ede6;
  }
  html, body { margin: 0; padding: 0; overflow: hidden; }
  .cup-wrap {
    position: relative;
    width: 1200px;
    height: 960px;
    background: var(--paper);
    overflow: hidden;
  }
  .badge { position: absolute; left: 0; top: 0; }
  .handle-tag {
    position: absolute;
    top: 300px;
    width: 26px;
    height: 200px;
    background: var(--brown);
    display: flex;
    align-items: center;
    justify-content: center;
  }
  .handle-tag--left { left: 326px; }
  .handle-tag--right { left: 848px; }
  .handle-tag__inner {
    transform: rotate(90deg);
    white-space: nowrap;
    display: flex;
    align-items: center;
    gap: 6px;
    color: var(--cream);
    font-family: "Josefin Sans", sans-serif;
    font-size: 15px;
    font-weight: 400;
    letter-spacing: 0.02em;
  }
  .handle-tag__dot {
    width: 9px; height: 9px;
    border: 1.5px solid var(--cream);
    border-radius: 50%;
  }
  .brand-name {
    position: absolute;
    left: 0; width: 1200px;
    top: 374px;
    text-align: center;
    font-family: "Josefin Sans", sans-serif;
    font-weight: 300;
    font-size: 40px;
    line-height: 1;
    letter-spacing: 0.08em;
    text-indent: 0.08em;
    color: var(--cream);
  }
  .brand-descriptor {
    position: absolute;
    left: 0; width: 1200px;
    top: 424px;
    text-align: center;
    font-family: "Josefin Sans", sans-serif;
    font-weight: 300;
    font-size: 13px;
    line-height: 1;
    letter-spacing: 0.05em;
    color: var(--cream);
  }
  .slogan {
    position: absolute;
    left: 0; width: 1200px;
    top: 700px;
    margin: 0;
    text-align: center;
    color: var(--brown);
    white-space: nowrap;
  }
  .slogan__script {
    font-family: "Dancing Script", cursive;
    font-size: 40px;
    margin-right: 10px;
  }
  .slogan__bold {
    font-family: "Josefin Sans", sans-serif;
    font-weight: 700;
    font-size: 42px;
    letter-spacing: 0.01em;
  }
</style>
</head>
<body>
<main class="cup-wrap">
  <svg class="badge" width="1200" height="960" viewBox="0 0 1200 960">
    <defs>
      <g id="scallop">
        <circle cx="600" cy="400" r="180"/>
        <circle cx="600" cy="230" r="36" transform="rotate(0 600 400)"/>
        <circle cx="600" cy="230" r="36" transform="rotate(22.5 600 400)"/>
        <circle cx="600" cy="230" r="36" transform="rotate(45 600 400)"/>
        <circle cx="600" cy="230" r="36" transform="rotate(67.5 600 400)"/>
        <circle cx="600" cy="230" r="36" transform="rotate(90 600 400)"/>
        <circle cx="600" cy="230" r="36" transform="rotate(112.5 600 400)"/>
        <circle cx="600" cy="230" r="36" transform="rotate(135 600 400)"/>
        <circle cx="600" cy="230" r="36" transform="rotate(157.5 600 400)"/>
        <circle cx="600" cy="230" r="36" transform="rotate(180 600 400)"/>
        <circle cx="600" cy="230" r="36" transform="rotate(202.5 600 400)"/>
        <circle cx="600" cy="230" r="36" transform="rotate(225 600 400)"/>
        <circle cx="600" cy="230" r="36" transform="rotate(247.5 600 400)"/>
        <circle cx="600" cy="230" r="36" transform="rotate(270 600 400)"/>
        <circle cx="600" cy="230" r="36" transform="rotate(292.5 600 400)"/>
        <circle cx="600" cy="230" r="36" transform="rotate(315 600 400)"/>
        <circle cx="600" cy="230" r="36" transform="rotate(337.5 600 400)"/>
      </g>
    </defs>
    <use href="#scallop" fill="var(--brown)"/>
    <g role="img" aria-label="Light coffee-themed pattern of cups, beans and pots inside the scalloped frame">
      <use href="#scallop" fill="var(--pattern)" transform="translate(600 400) scale(0.935) translate(-600 -400)"/>
    </g>
    <circle cx="600" cy="400" r="138" fill="var(--brown)"/>
    <circle cx="600" cy="400" r="126" fill="var(--charcoal)"/>
  </svg>

  <div class="handle-tag handle-tag--left">
    <div class="handle-tag__inner"><span class="handle-tag__dot"></span>@marlowbrewhouse</div>
  </div>
  <div class="handle-tag handle-tag--right">
    <div class="handle-tag__inner"><span class="handle-tag__dot"></span>@marlowbrewhouse</div>
  </div>

  <div class="brand-name">MARLOW</div>
  <div class="brand-descriptor">SPECIALTY COFFEE HOUSE</div>

  <p class="slogan"><span class="slogan__script">...the sip of</span><span class="slogan__bold">FRESHNESS</span></p>
</main>
</body>
</html>
```